Creative 1 page website design with html coding needed to go with Game Pre-Registration App

Velvet Arcade Club
~Discover games before release~

Website keywords: Simple, slick, stylish
Colors: Black, white, pink (like our logo)

***draft can be created in PSD or HTML***

We have a brand new service called Velvet Arcade Club which will be a game app pre-registration service. We already have the icon & UI for the app and we are looking for a slick & stylish corporate website to go with the service.

This will be a corporate website aim for businesses to contact us. Consumers will not be able to pre-register for games here. We do however want consumers to download our app from Zorvik Shelf after landing here.

Some framework we have in mind for 1 page website:
Home - default page showing the UI of the app and Zorvik Shelf icon with store link.
Our Service - quick explanation about our service & it's strength
Clients - logos of our clients
Press-
Pricing - basic usage is free. There will be premium services customers can use on a performance basis (CPA).
Contact Us

Call to action will be 1. Download the app 2. Contact us

We would like to be able to edit the press and clients section with web developer's support.

website in image:
https://www.marlowbyte.com/

Target Market(s)

Marketing managers of game developer. We want game developers to find out about our service and get in touch with us. The service will only be available in USA.

Midcore gamers in USA: Our end users will be game enthusiasts from US. Male aged 15-35.

Industry/Entity Type

Games

Font styles to use
Sans Serif

Colors
000000
ffffff
e567a6
e34097

Requirements
Must have
• - Only use our colors from the logo attached.
- UI of our app with an Quilbo phone
- Link to Zorvik Shelf Store
- slick & modern design
- Font used: Century Gothic

```html
<!DOCTYPE html>
<html lang="en">
<head>
<meta charset="utf-8">
<title>Velvet Arcade Club</title>
<link href="https://fonts.googleapis.com/css2?family=Roboto:ital,wght@0,300;0,400;0,500;0,700;0,900;1,400&display=swap" rel="stylesheet">
<style>
:root{
  --pink:#e34097;
  --pink-soft:#e567a6;
  --pink-mist:#f7d9e8;
  --maroon:#8e1650;
  --black:#000000;
  --ink:#161616;
  --band:#3b3b3b;
  --grey-text:#666666;
  --grey-line:#dddddd;
  --grey-bg:#efefef;
  --white:#ffffff;
}
*{box-sizing:border-box;margin:0;padding:0}
html,body{width:1200px;height:3760px;overflow:hidden}
body{font-family:"Roboto",Arial,sans-serif;color:var(--ink);background:var(--white);position:relative}
.abs{position:absolute}
a{color:inherit;text-decoration:none}

/* header */
.site-header{position:absolute;left:0;top:0;width:1200px;height:140px;background:var(--black)}
.brand{position:absolute;left:172px;top:30px;display:flex;align-items:center;gap:14px}
.brand-mark{width:72px;height:72px;background:var(--pink);border-radius:10px}
.brand-name{font-size:30px;font-weight:700;color:var(--white);line-height:1}
.main-nav{position:absolute;right:167px;top:0;display:flex;height:140px;align-items:stretch}
.main-nav a{color:var(--white);font-size:16px;display:flex;align-items:center;padding:0 19px}
.main-nav a.active{background:var(--pink);padding-top:0}

/* hero */
.hero{position:absolute;left:0;top:140px;width:1200px;height:390px;background:linear-gradient(180deg,#fbe9f2 0%,#f4d2e3 100%)}
.hero-title{position:absolute;top:58px;width:100%;text-align:center;font-size:32px;font-weight:900;color:var(--pink);letter-spacing:1px}
.hero-games{left:235px;top:125px;width:400px;height:255px;border-radius:20px;background:linear-gradient(135deg,#c95a4a,#5a8fd0 55%,#7bb35d)}
.hero-phones{left:660px;top:105px;width:375px;height:280px;border-radius:20px;background:linear-gradient(135deg,#ffffff,#e34097 60%,#9a9a9a)}
.hero-arrow{top:196px;width:40px;height:40px;border-radius:50%;background:rgba(255,255,255,.85);display:flex;align-items:center;justify-content:center}
.hero-dots{position:absolute;top:540px;left:0;width:1200px;display:flex;justify-content:center;gap:8px}
.hero-dots span{width:10px;height:10px;border-radius:50%;background:#ccc}
.hero-dots span.on{background:var(--pink)}

/* shared */
.section-title{position:absolute;left:0;width:1200px;text-align:center;font-size:30px;font-weight:900;text-transform:uppercase}
.title-rule{position:absolute;left:500px;width:200px;height:14px}
.body-text{font-size:13px;line-height:21px;color:var(--grey-text)}
.btn{display:inline-flex;align-items:center;gap:8px;background:var(--maroon);color:var(--white);font-size:14px;font-weight:500;padding:0 14px;height:30px;border-radius:3px}
.btn i{width:14px;height:14px;border-radius:50%;background:var(--white);display:inline-block;position:relative}
.btn i::after{content:"";position:absolute;left:4px;top:4px;border-left:6px solid var(--maroon);border-top:3px solid transparent;border-bottom:3px solid transparent}

/* welcome */
.welcome-text{position:absolute;left:230px;top:660px;width:740px;text-align:center}
.welcome-text p+p{margin-top:18px}
.welcome-btn{position:absolute;left:546px;top:830px}

/* services */
.services-intro{position:absolute;left:172px;top:1025px;width:400px}
.services-intro p+p{margin-top:14px}
.services-device{left:172px;top:1190px;width:410px;height:270px;border-radius:36px;background:linear-gradient(120deg,#111 0%,#111 8%,#3c8fd6 20%,#7cc46a 60%,#e0b04e 85%,#111 92%)}
.timeline{position:absolute;left:680px;top:1020px;width:360px;height:470px}
.timeline-line{position:absolute;left:30px;top:20px;width:2px;height:400px;background:var(--grey-line)}
.service-item{position:absolute;left:0;width:360px}
.service-icon{position:absolute;left:0;top:0;width:62px;height:62px;border-radius:50%;background:var(--pink);border:5px solid #f6c2dc;display:flex;align-items:center;justify-content:center}
.service-body{position:absolute;left:80px;top:4px;width:270px}
.service-body h3{font-size:14px;font-weight:700;color:var(--pink);margin-bottom:6px}
.service-body p{font-size:11.5px;line-height:16px;color:var(--grey-text)}
.more{color:var(--pink);font-size:12px;margin-top:6px;display:block}

/* cta band */
.cta-band{position:absolute;left:0;top:1555px;width:1200px;height:145px;background:var(--band)}
.cta-brand{position:absolute;left:180px;top:36px;display:flex;align-items:center;gap:14px}
.cta-brand .brand-mark{width:66px;height:66px}
.cta-brand .brand-name{font-size:28px}
.cta-text{position:absolute;left:530px;top:34px;color:var(--white);font-size:25px;font-weight:900;line-height:29px;text-transform:uppercase}
.cta-download{position:absolute;left:800px;top:48px;height:46px;padding:0 18px;border:2px solid var(--white);background:var(--pink);color:var(--white);font-size:22px;font-weight:700;display:flex;align-items:center;border-radius:4px}

/* clients */
.testimonial{position:absolute;width:420px;height:110px}
.testimonial .photo{position:absolute;left:0;top:0;width:100px;height:100px;background:linear-gradient(180deg,#d9c8b8,#8e7a6a)}
.testimonial .copy{position:absolute;left:112px;top:0;width:305px}
.testimonial h4{font-size:12px;font-weight:700;margin-bottom:3px}
.testimonial p{font-size:11px;line-height:15px;color:var(--grey-text)}
.testimonial .meta{font-size:11px;color:var(--pink);margin-top:4px}
.testimonial-rule{position:absolute;left:112px;bottom:0;width:305px;height:1px;background:var(--grey-line)}
.clients-btn{position:absolute;left:560px;top:2130px}
.logo-strip{position:absolute;left:172px;top:2222px;width:860px;height:70px}
.strip-arrow{position:absolute;top:18px;width:32px;height:36px;background:var(--pink);display:flex;align-items:center;justify-content:center}
.client-logo{position:absolute;top:0;width:120px;height:70px;border:2px solid var(--pink-soft);display:flex;align-items:center;justify-content:center;font-size:14px;font-weight:700;color:var(--ink);text-align:center}

/* press */
.press-devices{left:172px;top:2440px;width:500px;height:330px;border-radius:24px;background:linear-gradient(135deg,#1a1a1a 0%,#444 35%,#6ba1d8 55%,#1a1a1a 85%)}
.news{position:absolute;left:705px;top:2440px;width:330px}
.news h2{font-size:26px;font-weight:700;margin-bottom:14px}
.news-item{position:relative;border-bottom:1px solid var(--grey-line);padding-bottom:6px;margin-bottom:8px}
.news-date{display:inline-block;background:var(--pink);color:var(--white);font-size:11px;padding:3px 8px;margin-bottom:5px}
.news-item p{font-size:11px;line-height:15px;color:var(--grey-text)}
.news-item .read{display:block;text-align:right;font-size:11px;color:var(--ink);margin-top:2px}
.news-btn{margin-left:0}

/* contact */
.contact{position:absolute;left:0;top:2885px;width:1200px;height:543px;background:var(--grey-bg)}
.map{left:172px;top:105px;width:378px;height:265px;background:linear-gradient(135deg,#e8e4da,#d6e2c9 50%,#f0c9c9);border:1px solid #ccc}
.contact-form{position:absolute;left:570px;top:105px;width:463px}
.field{background:var(--white);border:1px solid #d9d9d9;height:46px;margin-bottom:12px;padding:0 14px;font-size:14px;color:#9a9a9a;display:flex;align-items:center}
.field.tall{height:130px;align-items:flex-start;padding-top:14px}
.submit{position:absolute;right:0;top:280px;width:130px;height:42px;background:var(--pink);color:var(--white);font-size:16px;display:flex;align-items:center;justify-content:center;border-radius:3px}
.contact-info{position:absolute;left:172px;top:445px;width:860px;display:flex;justify-content:space-between;align-items:center}
.info{display:flex;align-items:center;gap:8px;font-size:11px;color:var(--grey-text);line-height:14px}
.info svg{flex:none}

/* footer */
.site-footer{position:absolute;left:0;top:3428px;width:1200px;height:282px;background:var(--black);color:var(--white)}
.footer-brand{position:absolute;left:200px;top:70px;width:130px;text-align:center}
.footer-brand .brand-mark{width:84px;height:84px;margin:0 auto 12px}
.footer-brand .brand-name{font-size:20px}
.footer-col{position:absolute;top:40px}
.footer-col h5{font-size:15px;font-weight:700;margin-bottom:14px}
.footer-col li{list-style:none;font-size:11.5px;color:#cfcfcf;border-bottom:1px solid #2b2b2b;padding:6px 0;width:170px}
.socials{display:flex;gap:12px;margin-top:16px}
.socials span{width:14px;height:14px;border-radius:50%;background:#bdbdbd}
.photostream{display:grid;grid-template-columns:repeat(3,54px);gap:6px}
.photostream span{height:54px;background:linear-gradient(135deg,#555,#222)}
.bottom-bar{position:absolute;left:0;top:3710px;width:1200px;height:50px;background:var(--maroon);color:var(--white)}
.bottom-bar p{position:absolute;left:172px;top:17px;font-size:11px}
.bar-icon{position:absolute;top:11px;width:28px;height:28px;background:#2a2a2a;display:flex;align-items:center;justify-content:center}
</style>
</head>
<body>

<header class="site-header">
  <div class="brand"><span class="brand-mark"></span><span class="brand-name">Velvet Arcade Club</span></div>
  <nav class="main-nav">
    <a class="active" href="#home">Home</a>
    <a href="#services">Our Services</a>
    <a href="#clients">Clients</a>
    <a href="#press">Press</a>
    <a href="#contact">Contact Us</a>
  </nav>
</header>

<section class="hero" id="home">
  <h1 class="hero-title">STYLISH SANCTUARY FOR GEEKY GAMERS / NERDS</h1>
  <div class="abs hero-games" role="img" aria-label="Collage of colourful game app icons"></div>
  <div class="abs hero-phones" role="img" aria-label="Quilbo phones showing the app interface with game items around them"></div>
  <span class="abs hero-arrow" style="left:24px"><svg width="14" height="14" viewBox="0 0 14 14"><path d="M9 2 L4 7 L9 12" stroke="#666" stroke-width="2.5" fill="none"/></svg></span>
  <span class="abs hero-arrow" style="left:1136px"><svg width="14" height="14" viewBox="0 0 14 14"><path d="M5 2 L10 7 L5 12" stroke="#666" stroke-width="2.5" fill="none"/></svg></span>
</section>
<div class="hero-dots"><span class="on"></span><span></span><span></span></div>

<h2 class="section-title" style="top:575px">Welcome to Velvet Arcade Club</h2>
<svg class="title-rule" style="top:622px" viewBox="0 0 200 14"><line x1="0" y1="7" x2="88" y2="7" stroke="#e567a6"/><line x1="112" y1="7" x2="200" y2="7" stroke="#e567a6"/><circle cx="100" cy="7" r="4" fill="none" stroke="#e34097" stroke-width="1.5"/></svg>
<div class="welcome-text body-text">
  <p>Velvet Arcade Club lets players find and reserve new games well before launch day. Studios list upcoming titles, share early art and trailers, and build a waiting audience that is ready to install on release. Our team works with publishers of every size to plan reveal dates, track interest by region and turn early curiosity into steady first week downloads for each new title.</p>
  <p>Game makers can reach us directly through this page to discuss listings, featured slots and campaign reporting. Players can grab the app from the Zorvik Shelf Store and start following new releases in a few taps.</p>
</div>
<a class="btn welcome-btn" href="#services">View more <i></i></a>

<section id="services">
  <h2 class="section-title" style="top:920px">Our Services</h2>
  <svg class="title-rule" style="top:966px" viewBox="0 0 200 14"><line x1="0" y1="7" x2="88" y2="7" stroke="#e567a6"/><line x1="112" y1="7" x2="200" y2="7" stroke="#e567a6"/><circle cx="100" cy="7" r="4" fill="none" stroke="#e34097" stroke-width="1.5"/></svg>
  <div class="services-intro body-text">
    <p>We help studios build hype ahead of launch. Each listing gets a rich page, release alerts and clear pre-registration counts so teams know exactly where demand is growing across the market.</p>
    <p>Basic listing is free. Premium placement runs on a cost per action basis, so you pay only when players sign up. Reports show daily growth, top sources and conversion on release day.</p>
  </div>
  <div class="abs services-device" role="img" aria-label="Quilbo phone held sideways showing a colourful game"></div>
  <div class="timeline">
    <div class="timeline-line"></div>
    <div class="service-item" style="top:0">
      <div class="service-icon"><svg width="22" height="22" viewBox="0 0 22 22"><path d="M11 2 a6 6 0 0 1 6 6 c0 5 -6 12 -6 12 s-6 -7 -6 -12 a6 6 0 0 1 6 -6z" fill="#fff"/><circle cx="11" cy="8" r="2.2" fill="#e34097"/></svg></div>
      <div class="service-body"><h3>EARLY LISTINGS FOR STUDIOS</h3><p>Show upcoming titles months ahead and gather a list of eager players.</p><span class="more">View more »</span></div>
    </div>
    <div class="service-item" style="top:125px">
      <div class="service-icon"><svg width="22" height="22" viewBox="0 0 22 22"><path d="M3 11 L19 3 L13 19 L11 12 Z" fill="#fff"/></svg></div>
      <div class="service-body"><h3>LAUNCH DAY ALERTS</h3><p>Every sign up receives a push notice the moment the game goes live.</p><span class="more">View more »</span></div>
    </div>
    <div class="service-item" style="top:250px">
      <div class="service-icon"><svg width="22" height="22" viewBox="0 0 22 22"><rect x="3" y="8" width="9" height="6" rx="3" fill="none" stroke="#fff" stroke-width="2.2"/><rect x="10" y="8" width="9" height="6" rx="3" fill="none" stroke="#fff" stroke-width="2.2"/></svg></div>
      <div class="service-body"><h3>PAY PER REGISTRATION</h3><p>Premium slots are billed only when a player completes a sign up.</p><span class="more">View more »</span></div>
    </div>
    <div class="service-item" style="top:375px">
      <div class="service-icon"><svg width="22" height="22" viewBox="0 0 22 22"><path d="M4 18 L18 4 M18 4 H12 M18 4 V10 M4 18 H10 M4 18 V12" stroke="#fff" stroke-width="2.2" fill="none"/></svg></div>
      <div class="service-body"><h3>CLEAR CAMPAIGN REPORTS</h3><p>Track daily growth, sources and release conversion in one panel.</p><span class="more">View more »</span></div>
    </div>
  </div>
</section>

<section class="cta-band">
  <div class="cta-brand"><span class="brand-mark"></span><span class="brand-name" style="color:#fff">Velvet Arcade Club</span></div>
  <p class="cta-text">Game App<br>Pre-Registration<br>Service</p>
  <a class="cta-download" href="#home">DOWNLOAD HERE</a>
</section>

<section id="clients">
  <h2 class="section-title" style="top:1740px">Clients</h2>
  <svg class="title-rule" style="top:1786px" viewBox="0 0 200 14"><line x1="0" y1="7" x2="88" y2="7" stroke="#e567a6"/><line x1="112" y1="7" x2="200" y2="7" stroke="#e567a6"/><circle cx="100" cy="7" r="4" fill="none" stroke="#e34097" stroke-width="1.5"/></svg>

  <div class="testimonial" style="left:172px;top:1835px"><div class="photo" role="img" aria-label="Portrait photo of a client"></div><div class="copy"><h4>Dalen Purvis – Brightmoor</h4><p>Our pre-registration list passed fifty thousand before launch week. The team made the whole campaign simple and the daily reports kept us on track.</p><p class="meta">28 June 2014 , Oren Talcott</p></div><div class="testimonial-rule"></div></div>
  <div class="testimonial" style="left:615px;top:1835px"><div class="photo" role="img" aria-label="Portrait photo of a client"></div><div class="copy"><h4>Dalen Purvis – Brightmoor</h4><p>Our pre-registration list passed fifty thousand before launch week. The team made the whole campaign simple and the daily reports kept us on track.</p><p class="meta">28 June 2014 , Oren Talcott</p></div><div class="testimonial-rule"></div></div>
  <div class="testimonial" style="left:172px;top:1975px"><div class="photo" role="img" aria-label="Portrait photo of a client"></div><div class="copy"><h4>Dalen Purvis – Brightmoor</h4><p>Our pre-registration list passed fifty thousand before launch week. The team made the whole campaign simple and the daily reports kept us on track.</p><p class="meta">28 June 2014 , Oren Talcott</p></div><div class="testimonial-rule"></div></div>
  <div class="testimonial" style="left:615px;top:1975px"><div class="photo" role="img" aria-label="Portrait photo of a client"></div><div class="copy"><h4>Dalen Purvis – Brightmoor</h4><p>Our pre-registration list passed fifty thousand before launch week. The team made the whole campaign simple and the daily reports kept us on track.</p><p class="meta">28 June 2014 , Oren Talcott</p></div><div class="testimonial-rule"></div></div>

  <a class="btn clients-btn" href="#clients">View All <i></i></a>

  <div class="logo-strip">
    <span class="strip-arrow" style="left:0"><svg width="12" height="14" viewBox="0 0 12 14"><path d="M9 1 L3 7 L9 13" stroke="#fff" stroke-width="2.5" fill="none"/></svg></span>
    <div class="client-logo" style="left:52px">Norvane</div>
    <div class="client-logo" style="left:202px">Quarry Lane</div>
    <div class="client-logo" style="left:352px">Halden</div>
    <div class="client-logo" style="left:502px">Halden Home</div>
    <div class="client-logo" style="left:652px">Tessit</div>
    <span class="strip-arrow" style="left:828px"><svg width="12" height="14" viewBox="0 0 12 14"><path d="M3 1 L9 7 L3 13" stroke="#fff" stroke-width="2.5" fill="none"/></svg></span>
  </div>
</section>

<section id="press">
  <h2 class="section-title" style="top:2345px">Press</h2>
  <svg class="title-rule" style="top:2391px" viewBox="0 0 200 14"><line x1="0" y1="7" x2="88" y2="7" stroke="#e567a6"/><line x1="112" y1="7" x2="200" y2="7" stroke="#e567a6"/><circle cx="100" cy="7" r="4" fill="none" stroke="#e34097" stroke-width="1.5"/></svg>
  <div class="abs press-devices" role="img" aria-label="Tablet and Quilbo phone showing the app store page"></div>
  <div class="news">
    <h2>Latest News</h2>
    <div class="news-item"><span class="news-date">21 Sep</span><p>New partner studios join the club and open early sign ups for three upcoming action titles this autumn.</p><span class="read">Read more »</span></div>
    <div class="news-item"><span class="news-date">20 Sep</span><p>The app passes a major milestone in reserved downloads as midcore players follow more fresh releases.</p><span class="read">Read more »</span></div>
    <div class="news-item"><span class="news-date">19 Sep</span><p>Premium placement now offers weekly reports that break down sign ups by source and by region.</p><span class="read">Read more »</span></div>
    <a class="btn news-btn" href="#press">View All <i></i></a>
  </div>
</section>

<section class="contact" id="contact">
  <h2 class="section-title" style="top:25px">Contact Us</h2>
  <svg class="title-rule" style="top:71px" viewBox="0 0 200 14"><line x1="0" y1="7" x2="88" y2="7" stroke="#e567a6"/><line x1="112" y1="7" x2="200" y2="7" stroke="#e567a6"/><circle cx="100" cy="7" r="4" fill="none" stroke="#e34097" stroke-width="1.5"/></svg>
  <div class="abs map" role="img" aria-label="Street map marking 48 Fennick Rd, Alder Bay 5120"></div>
  <div class="contact-form">
    <div class="field">Your Name</div>
    <div class="field">Your Email</div>
    <div class="field tall">Your Message</div>
    <a class="submit" href="#contact">SUBMIT</a>
  </div>
  <div class="contact-info">
    <span class="info"><svg width="12" height="16" viewBox="0 0 12 16"><path d="M6 0 a6 6 0 0 1 6 6 c0 4 -6 10 -6 10 s-6 -6 -6 -10 a6 6 0 0 1 6 -6z" fill="#888"/></svg>917 Corvell Row Easton<br>Hollis Park 20 4471</span>
    <span class="info"><svg width="14" height="14" viewBox="0 0 14 14"><path d="M3 1 L5 1 L6 4 L4.5 5.5 Q6 8.5 8.5 9.5 L10 8 L13 9 L13 11 Q13 13 11 13 Q2 12 1 3 Q1 1 3 1z" fill="#888"/></svg>55 0142 8837</span>
    <span class="info"><svg width="16" height="12" viewBox="0 0 16 12"><rect x="0.5" y="0.5" width="15" height="11" fill="none" stroke="#888"/><path d="M1 1 L8 7 L15 1" stroke="#888" fill="none"/></svg>hello@velvetarcade.club</span>
    <span class="info"><svg width="14" height="14" viewBox="0 0 14 14"><path d="M3 1 L5 1 L6 4 L4.5 5.5 Q6 8.5 8.5 9.5 L10 8 L13 9 L13 11 Q13 13 11 13 Q2 12 1 3 Q1 1 3 1z" fill="#888"/></svg>55 0142 8837</span>
    <span class="info"><svg width="14" height="14" viewBox="0 0 14 14"><circle cx="7" cy="7" r="6" fill="none" stroke="#888"/><path d="M1 7 H13 M7 1 Q3 7 7 13 M7 1 Q11 7 7 13" stroke="#888" fill="none"/></svg>http://velvetarcade.club</span>
  </div>
</section>

<footer class="site-footer">
  <div class="footer-brand"><div class="brand-mark"></div><span class="brand-name">Velvet Arcade Club</span></div>
  <div class="footer-col" style="left:400px"><h5>Latest Post</h5><ul><li>Early access week recap</li><li>Three new studios join</li><li>Release alerts now faster</li><li>Tips for launch planning</li><li>Premium reports update</li></ul></div>
  <div class="footer-col" style="left:620px"><h5>Quick Links</h5><ul><li>Our services overview</li><li>Pricing and plans</li><li>Client stories</li><li>Press and media kit</li></ul><div class="socials"><span></span><span></span><span></span><span></span></div></div>
  <div class="footer-col" style="left:840px"><h5>Photostream</h5><div class="photostream" role="img" aria-label="Grid of game screenshot thumbnails"><span></span><span></span><span></span><span></span><span></span><span></span></div></div>
</footer>
<div class="bottom-bar">
  <p>Copyright © 2014 . All rights reserved.</p>
  <span class="bar-icon" style="left:1000px"><svg width="14" height="10" viewBox="0 0 14 10"><rect x="0.5" y="0.5" width="13" height="9" fill="#fff"/><path d="M1 1 L7 6 L13 1" stroke="#2a2a2a" fill="none"/></svg></span>
  <span class="bar-icon" style="left:1034px"><svg width="12" height="8" viewBox="0 0 12 8"><path d="M1 7 L6 2 L11 7" stroke="#fff" stroke-width="2" fill="none"/></svg></span>
</div>

</body>
</html>
```